Hearthstone & Basin Works Sales Flyer

We want a sales flyer that outlines our companies strengths with Kitchen & Bath Remodeling. We would like highlight those aspects while also showcasing our ability to do decks and home additions. We want financing packages to be a big part of the flyer.

Target Market(s)

Residential Customers

Requirements
Must have
• Financing options
Highlight Kitchen & bath remodeling
Less subtle is our decks and home additions
Nice to have
• Keep within our logo colors-we are looking for informative flyers that leave homeowners eager to call us after a meeting

```html
<!DOCTYPE html>
<html lang="en">
<head>
<meta charset="utf-8">
<title>Hearthstone &amp; Basin Works – Sales Flyer</title>
<link rel="stylesheet" href="https://fonts.googleapis.com/css2?family=Montserrat:wght@300;400;500;600;700&display=swap">
<style>
  :root {
    --navy: #0d1526;
    --orange: #f05a22;
    --blue: #1f74bd;
    --white: #ffffff;
    --backdrop: #e9e6e1;
  }
  * { box-sizing: border-box; margin: 0; padding: 0; }
  html, body {
    width: 1200px; height: 826px; overflow: hidden;
    background: var(--backdrop);
    font-family: "Montserrat", Arial, sans-serif;
  }
  .spread { position: relative; width: 1200px; height: 826px; }
  .page {
    position: absolute; top: 44px;
    width: 560px; height: 737px;
    overflow: hidden;
    background: var(--navy);
    box-shadow: 0 4px 14px rgba(0,0,0,.25);
  }
  .page--front { left: 26px; }
  .page--back { left: 614px; }
  .page__inner {
    position: absolute; left: 0; top: 0;
    width: 690px; height: 908px;
    transform: scale(0.8116); transform-origin: 0 0;
    color: var(--white);
  }
  .abs { position: absolute; }
  .shapes { position: absolute; left: 0; top: 0; width: 690px; height: 908px; }

  /* Front page */
  .brand-name {
    left: 0; width: 690px; top: 108px; text-align: center;
    font-weight: 700; font-size: 28px; letter-spacing: 0.5px;
    color: var(--orange); text-transform: uppercase;
  }
  .photo { position: absolute; }
  .photo--deck { left: 0; top: 170px; width: 352px; height: 217px;
    background: linear-gradient(160deg, #6d8a4a 0%, #8a7a66 45%, #5c5148 100%); }
  .photo--kitchen-wood { left: 352px; top: 170px; width: 338px; height: 217px;
    background: linear-gradient(135deg, #efeae2 0%, #d9cdb8 55%, #b48d5e 100%); }
  .photo--kitchen-white { left: 0; top: 387px; width: 352px; height: 215px;
    background: linear-gradient(90deg, #9a4a33 0%, #b6b3ae 22%, #eceae6 60%, #7a5d44 100%); }
  .photo--bathroom { left: 352px; top: 387px; width: 338px; height: 215px;
    background: linear-gradient(120deg, #b9c1cb 0%, #e4e8ee 55%, #ffffff 100%); }

  .about-title { left: 66px; top: 652px; font-weight: 300; font-size: 28px; }
  .about-text {
    left: 59px; top: 705px; width: 350px;
    font-size: 12.2px; line-height: 13.8px; font-weight: 400;
  }
  .service {
    position: absolute; left: 444px; width: 246px; height: 36px;
    display: flex; align-items: center; justify-content: center;
    font-weight: 600; font-size: 17px;
  }
  .service--remodel { top: 672px; background: var(--blue); }
  .service--finance { top: 720px; background: var(--orange); }
  .service-note { left: 444px; width: 246px; top: 777px; text-align: center; font-size: 12px; }

  /* Back page */
  .copy {
    left: 75px; width: 292px;
    font-size: 11.8px; line-height: 13.6px; text-align: justify;
  }
  .copy--one { top: 84px; }
  .copy--two { top: 248px; }
  .copy--three { top: 452px; }
  .photo--lit-kitchen { left: 416px; top: 96px; width: 274px; height: 570px;
    background: linear-gradient(170deg, #c7a6b0 0%, #8c6f98 30%, #3f3a8a 62%, #121a5e 100%); }
  .cta { left: 0; width: 680px; top: 750px; text-align: center; font-weight: 400; font-size: 28px; }
  .contact-row {
    left: 0; width: 690px; top: 812px;
    display: flex; justify-content: center; gap: 34px;
  }
  .contact { display: flex; align-items: center; gap: 10px; font-weight: 700; font-size: 14.5px; white-space: nowrap; }
  .contact__icon { width: 30px; height: 30px; flex: none; }
</style>
</head>
<body>
<main class="spread">

  <section class="page page--front">
    <div class="page__inner">
      <div class="photo photo--deck" role="img" aria-label="Photo of a two-storey wooden deck on a house"></div>
      <div class="photo photo--kitchen-wood" role="img" aria-label="Photo of a bright kitchen with wooden floor and table"></div>
      <div class="photo photo--kitchen-white" role="img" aria-label="Photo of a white kitchen with dining table beside a brick wall"></div>
      <div class="photo photo--bathroom" role="img" aria-label="Photo of a modern white bathroom with double basins"></div>

      <svg class="shapes" viewBox="0 0 690 908" aria-hidden="true">
        <polygon points="0,0 690,0 690,158 352,196 0,158" fill="var(--navy)"/>
        <polygon points="0,155 352,195 0,195" fill="var(--orange)"/>
        <polygon points="352,195 690,155 690,195" fill="var(--blue)"/>
        <polygon points="0,582 352,582 0,622" fill="var(--blue)"/>
        <polygon points="352,582 690,582 690,622" fill="var(--orange)"/>
        <polygon points="0,622 352,582 690,622 690,908 0,908" fill="var(--navy)"/>
      </svg>

      <div class="abs brand-name">Hearthstone &amp; Basin Works</div>

      <h2 class="abs about-title">About Us</h2>
      <p class="abs about-text">Lorem ipsum dolor sit amet, consectetur adipiscing elit. Fusce consectetur tellus sed purus tempor, ac tincidunt dolor pharetra. Quisque sodales ligula ante, sed pulvinar nunc vehicula at. Vivamus sit amet blandit sapien, in lacinia ipsum. Maecenas ultricies sem at urna consequat feugiat at sed mauris. Aliquam varius purus in vehicula tempor. Cras sagittis tincidunt neque, bibendum mollis tortor dapibus vel. Nam elementum elementum magna, in pulvinar diam pharetra vitae.</p>

      <div class="service service--remodel">Kitchen &amp; bath remodeling</div>
      <div class="service service--finance">Financing options</div>
      <p class="abs service-note">decks and home additions</p>
    </div>
  </section>

  <section class="page page--back">
    <div class="page__inner">
      <div class="photo photo--lit-kitchen" role="img" aria-label="Photo of a modern kitchen with bar stools and blue accent lighting"></div>

      <svg class="shapes" viewBox="0 0 690 908" aria-hidden="true">
        <polygon points="0,88 24,88 36,123 24,158 0,158" fill="var(--orange)"/>
        <polygon points="0,248 24,248 36,282 24,316 0,316" fill="var(--orange)"/>
        <polygon points="0,460 24,460 36,494 24,528 0,528" fill="var(--blue)"/>
        <polygon points="416,100 690,60 690,96 416,102" fill="var(--blue)"/>
        <polygon points="416,660 690,666 690,700" fill="var(--orange)"/>
      </svg>

      <p class="abs copy copy--one">Lorem ipsum dolor sit amet, consectetur adipiscing elit. Fusce consectetur tellus sed purus tempor, ac tincidunt dolor pharetra. Quisque sodales ligula ante, sed pulvinar nunc vehicula at. Vivamus sit amet blandit sapien, in lacinia ipsum. Maecenas ultricies sem at urna consequat feugiat at sed mauris. Aliquam varius purus in vehicula tempor. Cras sagittis tincidunt neque, bibendum mollis tortor dapibus vel. Nam elementum elementum magna, in pulvinar diam pharetra vitae.</p>
      <p class="abs copy copy--two">Phasellus feugiat quam id nibh blandit, tempus ornare eros volutpat. Cras scelerisque ipsum vitae ante consectetur sollicitudin. Suspendisse egestas, leo at ultricies molestie, mauris diam convallis eros, nec semper arcu leo at nulla. Suspendisse lobortis, lacus sit amet pretium condimentum, sem mauris finibus magna, sed eleifend nunc eros id nibh. Donec in accumsan enim. Vivamus malesuada ipsum mi, vel vehicula nunc condimentum at. Nunc sem eros, rhoncus nec dui ultricies, finibus tristique lorem. Nunc in faucibus nisi. Fusce consequat lectus eget tortor vestibulum, eu pulvinar erat ullamcorper.</p>
      <p class="abs copy copy--three">Quisque molestie consectetur eros, eu sodales enim cursus nec. Proin sed varius lacus. Donec mattis ex non tellus egestas, ac pulvinar erat ultricies. Aliquam a blandit arcu. Etiam blandit placerat pellentesque. Donec in ligula at eros efficitur luctus vel viverra turpis. Quisque quis laoreet ligula, quis scelerisque ligula. Donec id diam non dui ultrices suscipit. Aliquam eu mollis diam, vitae rhoncus lacus. Morbi lorem neque, eleifend vel imperdiet non, posuere eget ex. Donec tincidunt urna eu ante dapibus dictum. Quisque massa lectus, venenatis non velit sit amet,</p>

      <h2 class="abs cta">Contact us TODAY!</h2>

      <div class="abs contact-row">
        <div class="contact contact--web">
          <svg class="contact__icon" viewBox="0 0 30 30" aria-hidden="true">
            <circle cx="15" cy="15" r="15" fill="var(--orange)"/>
            <path d="M11 8 L20 16 L15.5 16.5 L18 21.5 L16 22.5 L13.6 17.5 L11 20 Z" fill="var(--white)"/>
          </svg>
          <span>www.hsbworks.com</span>
        </div>
        <div class="contact contact--phone">
          <svg class="contact__icon" viewBox="0 0 30 30" aria-hidden="true">
            <circle cx="15" cy="15" r="15" fill="var(--orange)"/>
            <rect x="10.5" y="6.5" width="9" height="17" rx="2" fill="var(--white)"/>
            <rect x="12" y="9" width="6" height="8" fill="var(--orange)"/>
            <circle cx="15" cy="20.5" r="1.2" fill="var(--orange)"/>
          </svg>
          <span>555-014-2290</span>
        </div>
        <div class="contact contact--mail">
          <svg class="contact__icon" viewBox="0 0 30 30" aria-hidden="true">
            <circle cx="15" cy="15" r="15" fill="var(--orange)"/>
            <rect x="7.5" y="9.5" width="15" height="11" fill="none" stroke="var(--white)" stroke-width="1.8"/>
            <path d="M7.5 9.5 L15 16 L22.5 9.5" fill="none" stroke="var(--white)" stroke-width="1.8"/>
          </svg>
          <span>hello@hsbworks.com</span>
        </div>
      </div>
    </div>
  </section>

</main>
</body>
</html>
```